Veltrano - Mechanic/Collision Center Business Card

We're looking for a business card design for our mechanic/ collision repair shop.

Can be with colours or monochromatic.

See the attached files.

Many thanks

```html
<!DOCTYPE html>
<html lang="en">
<head>
<meta charset="utf-8">
<title>Veltrano – Business Card</title>
<link rel="stylesheet" href="https://fonts.googleapis.com/css2?family=Roboto:wght@400;500;700;900&display=swap">
<style>
  :root {
    --page-bg: #e9e6e1;
    --card-front: #f3f3f3;
    --card-back: #2a2a2a;
    --ink: #1d2124;
    --ink-soft: #2b2e31;
    --silver: #cfcfcf;
    --accent-blue: #1e9fdc;
  }
  * { margin: 0; padding: 0; box-sizing: border-box; }
  html, body {
    width: 900px; height: 1200px; overflow: hidden;
    background: var(--page-bg);
    font-family: "Roboto", Arial, sans-serif;
  }
  .canvas { position: relative; width: 900px; height: 1200px; }
  .card {
    position: absolute; left: 75px; width: 768px;
    border-radius: 18px;
  }
  .card--front { top: 133px; height: 438px; background: var(--card-front); color: var(--ink); }
  .card--back { top: 627px; height: 441px; background: var(--card-back); }

  .contact-name {
    position: absolute; left: 38px; top: 36px;
    font-size: 28px; font-weight: 700; line-height: 1; letter-spacing: 0.3px;
  }
  .contact-role {
    position: absolute; left: 38px; top: 67px;
    font-size: 19px; font-weight: 400; line-height: 1;
  }
  .contact-phone {
    position: absolute; right: 41px; top: 39px;
    font-size: 21px; font-weight: 700; line-height: 1;
  }

  .brand-lockup {
    position: absolute; left: 0; right: 0;
    display: flex; align-items: center; justify-content: center;
  }
  .brand-mark { flex: none; border-radius: 50%; }
  .brand-name {
    font-weight: 900; line-height: 1; text-transform: uppercase;
  }
  .card--front .brand-lockup { top: 160px; height: 160px; gap: 22px; }
  .card--front .brand-mark { width: 86px; height: 86px; background: var(--accent-blue); }
  .card--front .brand-name { font-size: 96px; color: var(--ink); letter-spacing: 3px; }

  .card--back .brand-lockup { top: 170px; height: 170px; gap: 26px; }
  .card--back .brand-mark { width: 100px; height: 100px; background: var(--silver); }
  .card--back .brand-name { font-size: 114px; color: var(--silver); letter-spacing: 3px; }

  .contact-line {
    position: absolute; left: 0; right: 0; bottom: 30px;
    text-align: center; font-size: 20.5px; font-weight: 500; color: var(--ink-soft);
    white-space: nowrap;
  }
  .social-dot {
    position: absolute; top: 43px; right: 36px;
    width: 44px; height: 44px; border-radius: 50%;
    background: var(--accent-blue);
  }
</style>
</head>
<body>
<main class="canvas">
  <section class="card card--front">
    <h1 class="contact-name">MARCO FERREIRA</h1>
    <p class="contact-role">OWNER</p>
    <p class="contact-phone">+351 210 555 018</p>
    <div class="brand-lockup">
      <span class="brand-mark" aria-hidden="true"></span>
      <p class="brand-name">Veltrano</p>
    </div>
    <p class="contact-line">hello@veltrano-mail.com | Rua das Oficinas 14, Lisbon, Portugal</p>
  </section>
  <section class="card card--back">
    <span class="social-dot" role="img" aria-label="Social media link"></span>
    <div class="brand-lockup">
      <span class="brand-mark" aria-hidden="true"></span>
      <p class="brand-name">Veltrano</p>
    </div>
  </section>
</main>
</body>
</html>
```